Re-design of Business Card

We require a design for our business card.

Korrim is a supplier of industrial packaging specializing in plastic products. We are undergoing a rebranding to appear more corporate. We have changed our company name to korrim and have a new logo.

I have uploaded our old card design with the previous company name.
Don't copy the current design. We are looking for a new design.

Industry/Entity Type

Manufacturing

Contact Information for Business Card

please don't copy the current design. we are looking for a new design.

Font styles to use
Sans Serif

Colors

Designer to choose colors to be used in the design.

Requirements
Must have
• clean and easy to read.

```html
<!DOCTYPE html>
<html lang="en">
<head>
<meta charset="utf-8">
<title>Korrim Business Card</title>
<link href="https://fonts.googleapis.com/css2?family=Open+Sans:wght@400;600&display=swap" rel="stylesheet">
<style>
  :root {
    --page-bg: #d9d9d7;
    --card-bg: #231f20;
    --accent: #f47a20;
    --text-light: #f2f2f2;
    --text-muted: #d8d8d8;
  }
  * { margin: 0; padding: 0; box-sizing: border-box; }
  html, body {
    width: 1200px;
    height: 862px;
    overflow: hidden;
    background: var(--page-bg);
    font-family: "Open Sans", sans-serif;
  }
  .canvas {
    position: relative;
    width: 1200px;
    height: 862px;
  }
  .card {
    position: absolute;
    top: 272px;
    width: 520px;
    height: 318px;
    background: var(--card-bg);
    border-radius: 3px;
    box-shadow: 0 6px 18px rgba(0,0,0,0.25);
    overflow: hidden;
  }
  .card--front { left: 50px; }
  .card--back { left: 630px; }

  .brand-name {
    position: absolute;
    inset: 0;
    display: flex;
    align-items: center;
    justify-content: center;
    color: var(--accent);
    font-weight: 600;
    font-size: 66px;
    letter-spacing: 6px;
  }

  .accent-stripe {
    position: absolute;
    inset: 0;
    width: 520px;
    height: 318px;
  }
  .accent-stripe polygon { fill: var(--accent); }

  .person {
    position: absolute;
    left: 34px;
    top: 28px;
    color: var(--text-light);
  }
  .person__name {
    font-size: 22px;
    font-weight: 400;
    line-height: 1.2;
  }
  .person__title {
    color: var(--accent);
    font-size: 18px;
    line-height: 1.15;
    margin-bottom: 12px;
  }
  .person__contact {
    font-size: 13px;
    line-height: 1.75;
    color: var(--text-muted);
  }

  .office {
    position: absolute;
    right: 30px;
    top: 138px;
    text-align: right;
    color: var(--text-light);
  }
  .office__heading {
    font-size: 22px;
    line-height: 1.3;
    margin-bottom: 6px;
  }
  .office__details {
    font-size: 13px;
    line-height: 1.75;
    color: var(--text-muted);
  }
</style>
</head>
<body>
<main class="canvas">
  <section class="card card--front" aria-label="Card front">
    <div class="brand-name">KORRIM</div>
  </section>

  <section class="card card--back" aria-label="Card back">
    <svg class="accent-stripe" viewBox="0 0 520 318" aria-hidden="true">
      <polygon points="318,0 336,0 246,318 228,318"/>
    </svg>

    <div class="person">
      <p class="person__name">Dana Whitlock</p>
      <p class="person__title">Machinery Sales<br>Manager</p>
      <p class="person__contact">xxxx xxx xxx<br>dana@korrim.com.au</p>
    </div>

    <div class="office">
      <p class="office__heading">Main Office</p>
      <p class="office__details">
        48 Harlow St Kenmore Park<br>
        Qld 4070 Australia<br>
        Work: 1300 555 214<br>
        Mobile: +61 7 3555 0142<br>
        www.korrimpack.com.au
      </p>
    </div>
  </section>
</main>
</body>
</html>
```